Tobin Quartz Portal Page . It's guarantee project!

We need a clean and professional modern web application portal page
That includes the Login & Application Selection screen

Also, I need to design both Desktop and Mobile sizes.
We have an example design for our target

The application is Jetty Schedule and related data.
Our client is a bit conservative.

Theme color preferred : #00508B (main) #DF0D83 (secondary)

Target Market(s)

Oil & Fuel & Gasoline

Number of Pages Required

2 page

Font styles to use
Sans Serif

Colors
0054AA
0677BA
7BADD7
CADEEF
E8F1F8
E54698
E96AAD
F1A4CE
F9D9EA
FCEFF6

Requirements
Must have
• Login Page & Main Screen

```html
<!DOCTYPE html>
<html lang="en">
<head>
<meta charset="utf-8">
<title>Tobin Quartz — Web App Portal Sign In</title>
<link rel="stylesheet" href="https://fonts.googleapis.com/css2?family=Poppins:wght@400;500;600;700&display=swap">
<style>
  :root {
    --primary: #00508B;
    --secondary: #DF0D83;
    --text-dark: #111111;
    --text-muted: #6b6b6b;
    --border: #dcdcdc;
    --divider: #e2e2e2;
    --white: #ffffff;
    --social-a: #e3e8f4;
    --social-b: #dff2fc;
    --social-c: #fbe2e2;
  }
  * { box-sizing: border-box; margin: 0; padding: 0; }
  html, body { width: 1200px; height: 576px; overflow: hidden; }
  body { font-family: 'Poppins', sans-serif; background: var(--white); color: var(--text-dark); position: relative; }

  .hero-photo {
    position: absolute; left: 0; top: 0; width: 600px; height: 576px;
    background: linear-gradient(180deg, #2f8fe0 0%, #4aa7ea 20%, #1f6fa8 32%, #3a6d8e 45%, #c9782f 58%, #e0a24a 66%, #5b5a62 80%, #3d3a44 100%);
  }

  .portal { position: absolute; left: 684px; top: 0; width: 320px; }

  .brand { position: absolute; left: -3px; top: 46px; white-space: nowrap; }
  .brand-name { font-size: 36px; font-weight: 700; color: var(--primary); line-height: 1; letter-spacing: -0.3px; }
  .brand-tag { position: absolute; left: 137px; top: 35px; font-size: 13px; font-weight: 500; color: var(--text-dark); letter-spacing: 0.3px; }

  .welcome { position: absolute; top: 116px; font-size: 24px; font-weight: 500; white-space: nowrap; }
  .intro { position: absolute; top: 154px; font-size: 13.2px; color: var(--text-muted); white-space: nowrap; }

  .field-label { position: absolute; font-size: 12px; font-weight: 500; }
  .field { position: absolute; width: 299px; height: 40px; border: 1px solid var(--border); border-radius: 5px; display: flex; align-items: center; padding-left: 11px; gap: 6px; font-size: 11.2px; color: #8a8a8a; }
  .field svg { width: 14px; height: 14px; flex: none; }

  .options { position: absolute; top: 347px; width: 302px; display: flex; justify-content: space-between; align-items: center; font-size: 10.5px; }
  .remember { display: flex; align-items: center; gap: 6px; color: var(--text-muted); }
  .checkbox { width: 12px; height: 12px; border: 1px solid #bdbdbd; border-radius: 2px; }
  .forgot { color: var(--secondary); font-weight: 500; }

  .sign-in { position: absolute; top: 383px; width: 299px; height: 40px; background: var(--primary); color: var(--white); border-radius: 4px; display: flex; align-items: center; justify-content: center; font-size: 15px; font-weight: 500; }

  .signup { position: absolute; top: 443px; width: 300px; text-align: center; font-size: 10.5px; color: #333; }
  .signup span { color: var(--secondary); font-weight: 500; }

  .divider { position: absolute; top: 474px; left: -2px; width: 304px; display: flex; align-items: center; gap: 16px; font-size: 10px; color: #444; }
  .divider::before, .divider::after { content: ""; flex: 1; height: 1px; background: var(--divider); }

  .social { position: absolute; top: 502px; left: 99px; display: flex; gap: 8px; }
  .social-btn { width: 28px; height: 28px; border-radius: 3px; }
  .social-btn.one { background: var(--social-a); }
  .social-btn.two { background: var(--social-b); }
  .social-btn.three { background: var(--social-c); }
</style>
</head>
<body>
  <div class="hero-photo" role="img" aria-label="Harbour at dusk with container cranes, cargo ships and a cruise liner on calm blue water"></div>

  <main class="portal">
    <div class="brand">
      <div class="brand-name">Tobin Quartz</div>
      <div class="brand-tag">WEB APP PORTAL</div>
    </div>

    <h1 class="welcome">Welcome to Back!</h1>
    <p class="intro">Please sign in to your account and start the Portal</p>

    <label class="field-label" style="top:193px">Email or&nbsp; user Name</label>
    <div class="field" style="top:215px">
      <svg viewBox="0 0 16 16" fill="none" stroke="#555" stroke-width="1.2"><circle cx="8" cy="5" r="3"/><path d="M2.5 14.5c0-3 2.5-5 5.5-5s5.5 2 5.5 5z"/></svg>
      Type your username
    </div>

    <label class="field-label" style="top:271px">Password</label>
    <div class="field" style="top:293px">
      <svg viewBox="0 0 16 16" fill="none" stroke="#555" stroke-width="1.2"><rect x="3" y="7" width="10" height="8" rx="1.5"/><path d="M5 7V5a3 3 0 0 1 6 0v2"/><path d="M8 10v2"/></svg>
      <span style="letter-spacing:1px">*******************</span>
    </div>

    <div class="options">
      <div class="remember"><span class="checkbox"></span>Remember Me</div>
      <div class="forgot">Forgot Password?</div>
    </div>

    <div class="sign-in">SIGN IN</div>

    <p class="signup">New on our platform? <span>Create an account</span></p>

    <div class="divider">Or</div>

    <div class="social">
      <div class="social-btn one"></div>
      <div class="social-btn two"></div>
      <div class="social-btn three"></div>
    </div>
  </main>
</body>
</html>
```